New Poster Design for Film Festival

Hi! We need a poster design for our student film festival and the Thornfield State University. We screen over 300 short films over a 3 days in May. Our committee wants a look feel similar to the image we attached below.

Target Market(s)

Students and general audience.

Industry/Entity Type

Festival

Colors
3377b5
85abd2
34b8a4
f68e4e

Requirements
Must have
• Larkspur Film Festival
17th Annual
May 2-3-4 2014
Ada Penhallow Theatre
Free Admission
Department of Screen and Digital Storytelling

Poster size 36" (high) x 24" (wide)
Thornfield State University
www.larkspurfilmfest.example
Nice to have
• Bold lettering
Should not have
• Flamingos - hate them :)

```html
<!DOCTYPE html>
<html lang="en">
<head>
<meta charset="utf-8">
<title>Larkspur Film Festival Poster</title>
<link rel="stylesheet" href="https://fonts.googleapis.com/css2?family=Oswald:wght@500;600;700&family=Cabin:wght@500&display=swap">
<style>
  :root {
    --blue-deep: #3377b5;
    --blue-soft: #85abd2;
    --blue-faint: #c0d6ea;
    --orange: #f68e4e;
    --orange-pale: #fbd2b6;
    --cream: #f0ebd2;
    --white: #ffffff;
    --ink: #111111;
    --band-end: #b8babd;
  }
  html, body {
    margin: 0;
    padding: 0;
    overflow: hidden;
  }
  .canvas {
    position: relative;
    width: 1200px;
    height: 900px;
    background: var(--white);
    overflow: hidden;
    font-family: "Oswald", "Arial Narrow", sans-serif;
  }
  .feature-title {
    position: absolute;
    left: 70px;
    top: 200px;
    width: 600px;
    margin: 0;
    transform: rotate(-26deg);
    transform-origin: center;
    color: var(--blue-faint);
    text-align: center;
    text-transform: uppercase;
    line-height: 0.9;
  }
  .feature-title__name {
    display: block;
    font-weight: 700;
    font-size: 118px;
    letter-spacing: 2px;
  }
  .feature-title__sub {
    display: block;
    font-weight: 600;
    font-size: 64px;
    letter-spacing: 14px;
    margin-top: 6px;
  }
  .poster {
    position: absolute;
    left: 669px;
    top: 33px;
    width: 459px;
    height: 676px;
    border: 4px solid var(--ink);
    background: var(--white);
  }
  .poster__field {
    position: absolute;
    left: 27px;
    top: 18px;
    width: 400px;
    height: 515px;
    background: var(--cream);
    border-radius: 72px;
  }
  .poster__art {
    position: absolute;
    left: 0;
    top: 0;
    width: 459px;
    height: 676px;
  }
  .poster__title {
    position: absolute;
    left: 30px;
    top: 66px;
    margin: 0;
    transform: rotate(-16deg);
    transform-origin: left bottom;
    color: var(--blue-deep);
    text-transform: uppercase;
    line-height: 0.9;
  }
  .poster__title-name {
    display: block;
    font-weight: 700;
    font-size: 50px;
  }
  .poster__title-sub {
    display: block;
    font-weight: 600;
    font-size: 28px;
    letter-spacing: 2px;
  }
  .poster__annual {
    position: absolute;
    left: 310px;
    top: 66px;
    width: 94px;
    height: 94px;
    transform: rotate(-18deg);
    color: var(--cream);
    text-align: center;
    text-transform: uppercase;
    font-weight: 700;
    line-height: 1;
  }
  .poster__annual-th {
    display: block;
    font-size: 28px;
    margin-top: 6px;
  }
  .poster__annual-word {
    display: block;
    font-size: 15px;
    margin-top: 24px;
  }
  .poster__dates {
    position: absolute;
    left: 188px;
    top: 200px;
    margin: 0;
    transform: rotate(-16deg);
    color: var(--blue-deep);
    text-transform: uppercase;
    text-align: right;
    line-height: 0.88;
  }
  .poster__dates-month {
    display: block;
    font-weight: 700;
    font-size: 72px;
  }
  .poster__dates-days {
    display: block;
    font-weight: 700;
    font-size: 54px;
  }
  .poster__dates-note {
    display: block;
    font-weight: 600;
    font-size: 13px;
    margin-top: 4px;
  }
  .poster__venue {
    position: absolute;
    left: 0;
    top: 570px;
    width: 459px;
    margin: 0;
    text-align: center;
    color: var(--blue-soft);
  }
  .poster__venue-name {
    display: block;
    font-weight: 600;
    font-size: 37px;
    line-height: 1;
    text-transform: uppercase;
  }
  .poster__venue-dept {
    display: block;
    font-family: "Cabin", "Gill Sans", sans-serif;
    font-weight: 500;
    font-size: 16px;
    margin-top: 6px;
  }
  .poster__venue-info {
    display: block;
    font-family: "Cabin", "Gill Sans", sans-serif;
    font-weight: 500;
    font-size: 11px;
    margin-top: 5px;
  }
  .footer-band {
    position: absolute;
    left: 95px;
    top: 735px;
    width: 1105px;
    height: 130px;
    background: linear-gradient(90deg, var(--white) 0%, var(--band-end) 100%);
  }
</style>
</head>
<body>
  <main class="canvas">
    <h1 class="feature-title">
      <span class="feature-title__name">Larkspur</span>
      <span class="feature-title__sub">Film Festival</span>
    </h1>

    <article class="poster">
      <div class="poster__field"></div>

      <svg class="poster__art" viewBox="0 0 459 676" xmlns="http://www.w3.org/2000/svg">
        <defs>
          <linearGradient id="sevenTone" x1="0" y1="0" x2="0" y2="1">
            <stop offset="0" stop-color="#fde6d6"/>
            <stop offset="1" stop-color="#f9c6a5"/>
          </linearGradient>
        </defs>
        <polygon role="img" aria-label="Numeral one formed by an orange film strip"
                 fill="var(--orange)"
                 points="27,196 115,152 130,156 290,531 160,531 62,283 27,290"/>
        <polygon role="img" aria-label="Numeral seven filled with orange cinema icons: popcorn, ticket, camera, film reels, soda"
                 fill="url(#sevenTone)"
                 points="151,153 405,45 420,52 427,100 427,531 333,531 333,139 167,208"/>
        <circle cx="357" cy="113" r="47" fill="var(--orange)"/>
        <circle cx="357" cy="113" r="8" fill="none" stroke="var(--cream)" stroke-width="4"/>
      </svg>

      <h2 class="poster__title">
        <span class="poster__title-name">Larkspur</span>
        <span class="poster__title-sub">Film Festival</span>
      </h2>

      <div class="poster__annual">
        <span class="poster__annual-th">th</span>
        <span class="poster__annual-word">Annual</span>
      </div>

      <p class="poster__dates">
        <span class="poster__dates-month">May</span>
        <span class="poster__dates-days">2,3,4</span>
        <span class="poster__dates-note">Free Admission</span>
      </p>

      <p class="poster__venue">
        <span class="poster__venue-name">Ada Penhallow Theatre</span>
        <span class="poster__venue-dept">Department of Screen and Digital Storytelling</span>
        <span class="poster__venue-info">Thornfield State University · 2014 · www.larkspurfilmfest.example</span>
      </p>
    </article>

    <div class="footer-band"></div>
  </main>
</body>
</html>
```